Buch-/E-Book-Cover für Finanzratgeber
Zielgruppe
Wir helfen Menschen dabei, ihr Geld vor der Inflation und den nahenden Enteignung zu schützen.
Aufgabenstellung
Orientierung an den Bestsellern von Finanzprodukten. Komplementärfarben, soll Neugierig machen.

```html
<!DOCTYPE html>
<html lang="de">
<head>
<meta charset="utf-8">
<title>Werden sie uns alles wegnehmen? – Buchumschlag</title>
<link href="https://fonts.googleapis.com/css2?family=Antonio:wght@400;600;700&family=Open+Sans:wght@400;700&display=swap" rel="stylesheet">
<style>
  :root {
    --stage: #e8e4dc;
    --paper: #fdf7ea;
    --crimson: #c8193f;
    --orange: #f0902a;
    --navy: #1d2036;
    --cream: #fdf7ea;
    --art-a: #e9e8e4;
    --art-b: #d9c3c4;
  }
  * { margin: 0; padding: 0; box-sizing: border-box; }
  html, body {
    width: 1200px; height: 511px; overflow: hidden;
    background: var(--stage);
  }
  .wrap {
    position: absolute; left: 204px; top: 0;
    width: 791px; height: 511px;
    background: var(--paper);
    overflow: hidden;
  }
  .display { font-family: "Antonio", "Arial Narrow", sans-serif; font-weight: 700; }
  .brand-box {
    position: absolute; background: var(--orange);
    display: flex; align-items: center; justify-content: center; gap: 4px;
    color: var(--cream); font-family: "Open Sans", Arial, sans-serif; font-weight: 400;
  }
  .brand-box .dot { border-radius: 50%; background: var(--cream); }

  /* Rückseite */
  .back-title {
    position: absolute; left: 60px; top: 64px;
    font-size: 22px; line-height: 1; white-space: nowrap;
    transform: scaleX(0.76); transform-origin: left top;
  }
  .back-title .a { color: var(--crimson); }
  .back-title .b { color: var(--orange); font-weight: 600; }
  .blurb {
    position: absolute; left: 60px; top: 108px; width: 240px;
    font-family: "Open Sans", Arial, sans-serif; font-size: 8.3px; line-height: 10.1px;
    color: var(--crimson);
  }
  .blurb p { margin-bottom: 10px; }
  .blurb strong { font-weight: 700; }
  .back-brand { left: 60px; top: 439px; width: 84px; height: 35px; font-size: 11px; }
  .back-brand .dot { width: 14px; height: 14px; }

  /* Rücken */
  .spine {
    position: absolute; left: 349px; top: 4px; width: 34px; height: 507px;
    background: var(--orange);
  }
  .spine-title {
    position: absolute; left: 8px; top: 39px;
    writing-mode: vertical-rl;
    font-size: 18px; line-height: 18px; color: var(--cream); white-space: nowrap;
    transform: scaleY(0.8); transform-origin: left top;
  }
  .spine-brand {
    position: absolute; left: 0; top: 397px; width: 34px;
    display: flex; flex-direction: column; align-items: center; gap: 5px;
    color: var(--cream);
    font-family: "Open Sans", Arial, sans-serif; font-size: 10px;
  }
  .spine-brand .dot { width: 16px; height: 16px; border-radius: 50%; background: var(--cream); }
  .spine-brand .name { writing-mode: vertical-rl; }

  /* Vorderseite */
  .front-brand { left: 631px; top: 3px; width: 90px; height: 34px; font-size: 11px; }
  .front-brand .dot { width: 14px; height: 14px; }
  .front-title-1 {
    position: absolute; left: 443px; top: 43px;
    font-size: 88px; line-height: 1; color: var(--crimson); white-space: nowrap;
    transform: scaleX(0.78); transform-origin: left top;
  }
  .front-title-2 {
    position: absolute; left: 446px; top: 134px;
    font-size: 42px; line-height: 1; color: var(--orange); font-weight: 600; white-space: nowrap;
    transform: scaleX(0.82); transform-origin: left top;
  }
  .cover-art {
    position: absolute; left: 465px; top: 180px; width: 226px; height: 266px;
    background: linear-gradient(160deg, var(--art-a) 0%, var(--art-a) 55%, var(--art-b) 100%);
  }
  .tagline {
    position: absolute; left: 400px; top: 465px; width: 366px; text-align: center;
    font-family: "Antonio", "Arial Narrow", sans-serif; font-weight: 600;
    font-size: 18px; line-height: 1; color: var(--navy); white-space: nowrap;
    transform: scaleX(0.7); transform-origin: center top;
  }
</style>
</head>
<body>
  <div class="wrap">
    <!-- Rückseite -->
    <h2 class="back-title display"><span class="a">WERDEN SIE</span> <span class="b">UNS ALLES WEGNEHMEN?</span></h2>
    <div class="blurb">
      <p>Es ist jetzt Zeit zu Handel und sich mit dem Thema Finanzen auseinander zu setzen. Wir befinden uns in der größten Umverteilung von Geld in der gesamten Geschichte. Wer die finanzielle Eigenverantwortung nicht übernimmt, der wird definitiv als Verlierer Nachhause gehen. Und wir reden hier nicht nur von ein paar Euro, sondern möglicherweise von allem was man besitzt.</p>
      <p>Du findest in diesem Buch den geschichtlichen Hintergrund zum Geldsystem, erfährst alles über Inflation und die aktuelle Finanzpolitik. Wir geben konkrete Lösungen, aus unserer gelebten 25 jährigen Finanzerfahrung.</p>
      <p>Wir liefern Dir Fakten z.B. zum Thema Enteignung, welche vor Corona noch als wilde Versicherungstheorie gegolten hätte.</p>
      <p><strong>Du willst Dein Kapital sichern, willst das System verstehen, möchtest wissen welche Rolle Gold und Rohstoffe spielen und das Ganze kurz und verständlich?</strong></p>
      <p><strong>Dann ist das Dein Buch!</strong></p>
    </div>
    <div class="brand-box back-brand"><span class="dot"></span>Kornwerk</div>

    <!-- Rücken -->
    <div class="spine">
      <div class="spine-title display">WERDEN SIE UNS ALLES WEGNEHMEN</div>
      <div class="spine-brand"><span class="dot"></span><span class="name">Kornwerk</span></div>
    </div>

    <!-- Vorderseite -->
    <div class="brand-box front-brand"><span class="dot"></span>Kornwerk</div>
    <h1 class="front-title-1 display">WERDEN SIE</h1>
    <div class="front-title-2 display">UNS ALLES WEGNEHMEN?</div>
    <div class="cover-art" role="img" aria-label="Illustration: zwei Männer auf kariertem Papier geben sich die Hand, während der Mann in Rot mit einem langen Arm dem anderen den Geldbeutel aus der Tasche zieht"></div>
    <p class="tagline">Jetzt das Finanz-System verstehen und Ihr Kapital sichern!</p>
  </div>
</body>
</html>
```